依頼詳細
◆サイトマップ
01.ホーム
02.当院について
03.医院紹介
04.スタッフ紹介
05.初めての方へ
06.銀歯から自然な白い歯へ
07.歯医者にいけなくなった方へ
08.歯の色を全体的に白くしたい方へ
09.口臭が気になる・歯茎に違和感がある
10.歯並びを整えたい方へ
11.歯が失ってしまった方へ
12.虫歯になってしまった方へ
13.お子様の歯を守りたい方へ
14.求人情報
15.よくあるご質問
16.問い合わせ
17.お知らせ(一覧)
18.お知らせ(詳細)
19.ブログ(一覧)
20.ブログ(詳細)

◆TOPに掲載いただきたいもの
・ヘッダー、ロゴ、営業時間、電話番号
・グローバルナビ
・メインイメージ
・お知らせの新着ボックス
・コンセプト
・強み
・各症状ページへ流入する箇所(サイトマップ06~13の内容)
・その他下層ページ移行用バナー(よくあるご質問、問い合わせ、求人情報)
・ブログの新着ボックス
・グーグルマップ
・フッター(ロゴ、院情報、営業時間、サイトマップ)
※仮で作成したもののためレイアウトの並びはお任せ致します。
ただし、配置してあるコンテンツはすべて含まれるようにしてください。
提案で項目を追加頂く等は参考にさせて頂きたいので大変嬉しいです。

◆デザインについて
・希望するイメージ
知的/清潔な/高級感

・希望デザインカラー
茶系
ベースは白やベージュ系

◆参考URL
https://miharadentalroom.example/
スペースのとり方に高級感を感じとても見やすい印象
TOPのコンテンツ量が少ないと感じる
サイトURL
http://203.0.113.47
ページ数
1ページ
希望イメージ
シンプル 複雑
単色 カラフル
暗い 明るい
日常 高級
遊び心 厳粛
未来的 伝統的
女性的 男性的
希望する色
茶系、ベースは白やベージュ系
納品ファイル
• イラストレーター形式 (.ai)
• フォトショップ形式 (.psd)
補足説明
◆素材について
素材として必要なものがある場合には、Lumira Stock画像をご使用ください。
その際、通常アセットでダウンロード出来る画像のみを使用してください。
Lumira Stock以外の素材を使用する際には、
必ず無料で提供いただける物のみご使用ください。
※現在、写真の用意がないのですが、撮影後に差し替える予定です。
イメージとしてLumira Stock画像を使用して作成ください。

◆ロゴ、外観、内観写真について
下記よりダウンロードしてご使用ください。
https://27.fileparcel.example/0811-b83c572e19a04df6c8e1b7a45d20e3f18
PASS:krvo
もう少し提案が見たいため、延長させて頂きます。
参考サイトを無視した少し奇抜なアイデアも見てみたいです。

院内で検討の上、決定致しました。
修正等も快諾いただき大変助かりました。

皆様たくさんのご提案ありがとうございました。

```html
<!DOCTYPE html>
<html lang="ja">
<head>
<meta charset="utf-8">
<title>KOYOMIDAI DENTAL</title>
<link href="https://fonts.googleapis.com/css2?family=Cormorant+Garamond:wght@400;500;600&family=Noto+Serif+JP:wght@400;500;600&family=Noto+Sans+JP:wght@300;400;500&display=swap" rel="stylesheet">
<style>
:root{
  --brown:#a48b68;
  --brown-dark:#7d6749;
  --brown-deep:#5f4c35;
  --beige:#f4f0ea;
  --beige-mid:#e9e1d5;
  --line:#d9cfc1;
  --ink:#3b3631;
  --ink-soft:#6e665d;
  --white:#ffffff;
  --serif:"Noto Serif JP", serif;
  --latin:"Cormorant Garamond", serif;
  --sans:"Noto Sans JP", sans-serif;
}
*{box-sizing:border-box;margin:0;padding:0}
html,body{width:1200px;height:4004px;overflow:hidden}
body{background:var(--white);color:var(--ink);font-family:var(--sans);font-size:13px;line-height:1.8;position:relative}
.abs{position:absolute}

/* header */
.site-header{position:absolute;left:0;top:0;width:1200px;height:72px;z-index:5}
.brand{position:absolute;left:48px;top:26px;display:flex;align-items:center;gap:10px;color:var(--white);font-family:var(--sans);font-weight:500;font-size:16px;letter-spacing:.06em;line-height:1}
.brand i{display:block;width:10px;height:10px;background:var(--white)}
.header-tools{position:absolute;right:72px;top:0;height:60px;background:var(--white);display:flex;align-items:center;gap:26px;padding:0 28px;font-size:14px;color:var(--ink)}
.header-tools span{display:flex;align-items:center;gap:6px}
.header-tools .access{font-size:11px}
.menu-btn{position:absolute;right:0;top:0;width:72px;height:72px;background:var(--brown-deep);color:var(--white);display:flex;flex-direction:column;align-items:center;justify-content:center;gap:5px;font-family:var(--latin);font-size:10px;letter-spacing:.2em}
.menu-btn i{display:block;width:24px;height:1px;background:var(--white)}

/* hero */
.hero{position:absolute;left:0;top:0;width:1120px;height:480px;background:linear-gradient(120deg,#d9cdbb 0%,#f3ede4 40%,#c8b79d 75%,#8f7a5e 100%)}
.hero-caption{position:absolute;left:250px;top:438px;background:rgba(95,76,53,.85);color:var(--white);font-family:var(--serif);font-size:14px;letter-spacing:.1em;padding:10px 26px}

/* info */
.sec-label{font-family:var(--latin);font-size:11px;letter-spacing:.25em;color:var(--brown)}
.info{position:absolute;top:520px;left:0;width:1200px;height:360px}
.news{position:absolute;left:130px;top:100px;width:420px}
.news li{list-style:none;display:flex;gap:22px;font-size:12px;padding:16px 0;border-bottom:1px solid var(--line)}
.news time{color:var(--ink-soft);font-family:var(--latin);font-size:13px}
.more-btn{display:flex;align-items:center;justify-content:center;gap:10px;width:150px;height:36px;border:1px solid var(--ink-soft);font-family:var(--latin);font-size:11px;letter-spacing:.25em}
.schedule{position:absolute;left:620px;top:100px;width:460px}
.schedule table{width:100%;border-collapse:collapse;font-size:12px;text-align:center}
.schedule th,.schedule td{padding:10px 0;border-bottom:1px solid var(--line);font-weight:400}
.schedule th:first-child,.schedule td:first-child{text-align:left;width:110px}
.schedule .note{font-size:11px;color:var(--ink-soft);margin-top:10px}

/* features */
.feature{position:absolute;left:0;width:1200px}
.feature h2{font-family:var(--serif);font-size:20px;font-weight:500;letter-spacing:.08em;margin:8px 0 18px}
.feature p{font-size:12px;color:var(--ink-soft);line-height:2.1}
.f1{top:912px;height:360px;background:var(--beige)}
.f1 .text{position:absolute;left:130px;top:90px;width:520px}
.f1 .photo{position:absolute;right:0;top:0;width:480px;height:370px;background:linear-gradient(160deg,#e8e1d5,#bda98a 60%,#6d5a42)}
.f2{top:1300px;height:350px;background:var(--white)}
.f2 .photo{position:absolute;left:0;top:0;width:580px;height:340px;background:linear-gradient(110deg,#7f6a4e,#d8c8ac 55%,#efe7da)}
.f2 .text{position:absolute;left:640px;top:80px;width:470px}
.vision{top:1660px;height:360px;background:linear-gradient(90deg,#b79f7e,#9c8463)}
.vision .box{position:absolute;left:120px;top:34px;width:600px;height:300px;border:1px solid rgba(255,255,255,.55);color:var(--white);padding:48px 60px}
.vision .sec-label{color:#f1e8da}
.vision h2{color:var(--white)}
.vision ol{list-style:none;font-family:var(--serif);font-size:14px;letter-spacing:.06em}
.vision li{padding:9px 0;border-bottom:1px solid rgba(255,255,255,.35)}
.vision .photo{position:absolute;right:0;top:0;width:480px;height:360px;background:linear-gradient(180deg,#3d4a5c,#7b8697 45%,#c9c0b1)}

/* symptoms */
.symptoms{position:absolute;top:2120px;left:0;width:1200px;height:360px;text-align:center}
.sec-title{font-family:var(--serif);font-size:20px;font-weight:500;letter-spacing:.12em}
.sec-title::after{content:"";display:block;width:40px;height:1px;background:var(--brown);margin:12px auto 0}
.symptom-grid{position:absolute;left:188px;top:110px;width:812px;display:grid;grid-template-columns:1fr 1fr;column-gap:32px;row-gap:16px}
.symptom-grid a{display:flex;justify-content:space-between;align-items:center;height:46px;padding:0 20px;border:1px solid var(--line);text-decoration:none;color:var(--ink);font-size:12px;text-align:left}
.symptom-grid a::after{content:"›";color:var(--brown);font-size:18px}

/* blog */
.blog{position:absolute;top:2520px;left:0;width:1200px;height:480px;background:var(--beige)}
.blog .head{position:absolute;left:0;top:30px;width:1200px;text-align:center}
.slider-nav{position:absolute;right:160px;top:88px;display:flex;gap:4px}
.slider-nav span{width:18px;height:18px;border:1px solid var(--line);background:var(--white);font-size:10px;display:flex;align-items:center;justify-content:center}
.slider-nav span.on{background:var(--brown);color:var(--white);border-color:var(--brown)}
.cards{position:absolute;left:160px;top:120px;display:flex;gap:20px}
.card{width:196px;background:var(--white)}
.card .thumb{height:130px}
.card .body{padding:12px 14px 14px}
.card time{font-family:var(--latin);font-size:11px;color:var(--ink-soft)}
.card h3{font-family:var(--serif);font-weight:500;font-size:12px;line-height:1.7;margin:4px 0 8px}
.card .read{font-family:var(--latin);font-size:10px;letter-spacing:.2em;text-align:right;color:var(--brown)}
.blog .more-btn{position:absolute;left:460px;top:420px;width:280px;background:var(--white)}

/* banners */
.banners{position:absolute;top:3088px;left:0;width:1200px;height:104px;display:flex}
.banners a{flex:1;display:flex;flex-direction:column;align-items:center;justify-content:center;gap:8px;color:var(--white);text-decoration:none;font-family:var(--serif);font-size:13px;letter-spacing:.1em}
.banners a:nth-child(1){background:#9d8665}
.banners a:nth-child(2){background:#b39c7a}
.banners a:nth-child(3){background:#c6b191}

/* access */
.access-sec{position:absolute;top:3228px;left:0;width:1200px;height:380px}
.map{position:absolute;left:40px;top:0;width:780px;height:370px;background:linear-gradient(135deg,#e7e4dc,#d6d9d3 50%,#e4ddcf)}
.clinic{position:absolute;left:860px;top:10px;width:300px}
.clinic .name{display:flex;align-items:center;gap:10px;font-family:var(--sans);font-weight:500;font-size:22px;color:var(--brown-dark);letter-spacing:.04em;line-height:1.2}
.clinic .name i{display:block;width:12px;height:12px;background:var(--brown-dark);flex:none}
.clinic .addr{font-size:11px;margin-top:16px;color:var(--ink-soft)}
.clinic .tel{font-family:var(--latin);font-size:22px;margin-top:4px;display:flex;align-items:center;gap:6px}
.clinic .hours{font-size:11px;margin:6px 0 10px}
.clinic table{width:100%;border-collapse:collapse;font-size:10px;text-align:center}
.clinic td,.clinic th{padding:6px 0;border-bottom:1px solid var(--line);font-weight:400}
.clinic td:first-child,.clinic th:first-child{text-align:left;width:80px}

/* footer */
.site-footer{position:absolute;top:3620px;left:0;width:1200px;height:384px;background:var(--beige-mid)}
.foot-nav{position:absolute;left:300px;top:70px;display:flex;gap:50px;font-size:11px}
.foot-nav ul{list-style:none}
.foot-nav li{line-height:2.3}
.copy{position:absolute;left:0;bottom:26px;width:1200px;text-align:center;font-family:var(--latin);font-size:10px;letter-spacing:.2em;color:var(--ink-soft)}
</style>
</head>
<body>

<header class="site-header">
  <div class="brand"><i></i>KOYOMIDAI DENTAL</div>
  <div class="header-tools">
    <span><svg width="14" height="14" viewBox="0 0 24 24"><path d="M6.6 10.8a15 15 0 0 0 6.6 6.6l2.2-2.2a1 1 0 0 1 1-.25 11.4 11.4 0 0 0 3.6.57 1 1 0 0 1 1 1V20a1 1 0 0 1-1 1A17 17 0 0 1 3 4a1 1 0 0 1 1-1h3.5a1 1 0 0 1 1 1c0 1.25.2 2.45.57 3.6a1 1 0 0 1-.25 1z" fill="#5f4c35"/></svg>03-5550-2184</span>
    <span class="access"><svg width="12" height="14" viewBox="0 0 24 28"><path d="M12 0a10 10 0 0 0-10 10c0 7 10 18 10 18s10-11 10-18A10 10 0 0 0 12 0zm0 14a4 4 0 1 1 0-8 4 4 0 0 1 0 8z" fill="#5f4c35"/></svg>アクセス</span>
  </div>
  <div class="menu-btn"><i></i><i></i><i></i>MENU</div>
</header>

<section class="hero" role="img" aria-label="明るく上質な受付カウンターと待合スペースの写真">
  <p class="hero-caption">最高峰の医療機器と最先端の技術で、ベストな治療を提供します。</p>
</section>

<section class="info">
  <div class="news">
    <p class="sec-label">INFORMATION</p>
    <ul style="margin-top:10px">
      <li><time>2020.03.10</time>お知らせの記事タイトルが入ります</li>
      <li><time>2020.03.05</time>お知らせの記事タイトルが入ります</li>
      <li><time>2020.02.21</time>お知らせの記事タイトルが入ります</li>
    </ul>
    <a class="more-btn" style="margin:34px auto 0;color:var(--ink);text-decoration:none">MORE ›</a>
  </div>
  <div class="schedule">
    <p class="sec-label">SCHEDULE</p>
    <table style="margin-top:10px">
      <tr><th></th><th>月</th><th>火</th><th>水</th><th>木</th><th>金</th><th>土</th><th>日</th><th>祝</th></tr>
      <tr><td>09:30 - 13:00</td><td>○</td><td>○</td><td>○</td><td>－</td><td>○</td><td>○</td><td>－</td><td>－</td></tr>
      <tr><td>14:30 - 19:00</td><td>○</td><td>○</td><td>○</td><td>－</td><td>○</td><td>△</td><td>－</td><td>－</td></tr>
    </table>
    <p class="note">休診日：木曜日、日曜日、祝日　／　△ 土曜午後は17:00まで</p>
  </div>
</section>

<section class="feature f1">
  <div class="text">
    <p class="sec-label">FEATURE 01</p>
    <h2>最先端の技術と安心の診療</h2>
    <p>当院では一人ひとりに合わせた、最適な歯科治療を提供しています。<br>丁寧なカウンセリングと確かな技術で、患者さまの不安に寄り添い、<br>痛みの少ない治療を心がけております。</p>
    <p style="margin-top:14px">また、院内は清潔に保ち、安心して通える環境を整えています。<br>小さなお悩みでもお気軽にご相談ください。</p>
  </div>
  <div class="photo" role="img" aria-label="白い診療チェアが置かれた個室診療室の写真"></div>
</section>

<section class="feature f2">
  <div class="photo" role="img" aria-label="間接照明が灯る落ち着いた待合室の写真"></div>
  <div class="text">
    <p class="sec-label">FEATURE 02</p>
    <h2>居心地のいい空間の提供</h2>
    <p>木目調の内装とやわらかな照明で、緊張をほぐす空間をご用意しました。<br>待ち時間もくつろいでお過ごしいただけます。</p>
    <p style="margin-top:14px">また、プライバシーに配慮した個室で落ち着いて治療を受けられます。<br>お子さま連れの方も安心してご来院ください。</p>
  </div>
</section>

<section class="feature vision">
  <div class="box">
    <p class="sec-label">VISION</p>
    <h2>わたしたちのビジョン</h2>
    <ol>
      <li>1．みんなが笑顔で通える歯科医院</li>
      <li>2．常に進化し続ける、安心の歯科医療を提供する</li>
      <li>3．最良の患者満足度を追求する</li>
    </ol>
  </div>
  <div class="photo" role="img" aria-label="夕暮れに照らされた医院外観の写真"></div>
</section>

<section class="symptoms">
  <p class="sec-label" style="margin-top:10px">MENU</p>
  <h2 class="sec-title">症状一覧</h2>
  <nav class="symptom-grid">
    <a href="#">銀歯から自然な白い歯へ</a>
    <a href="#">歯医者にいけなくなった方へ</a>
    <a href="#">歯の色を全体的に白くしたい方へ</a>
    <a href="#">口臭が気になる・歯茎に違和感がある方へ</a>
    <a href="#">歯並びを整えたい方へ</a>
    <a href="#">歯が失ってしまった方へ</a>
    <a href="#">虫歯になってしまった方へ</a>
    <a href="#">お子様の歯を守りたい方へ</a>
  </nav>
</section>

<section class="blog">
  <div class="head"><p class="sec-label">BLOG</p><h2 class="sec-title">スタッフブログ</h2></div>
  <div class="slider-nav"><span>‹</span><span class="on">›</span></div>
  <div class="cards">
    <article class="card"><div class="thumb" role="img" aria-label="歯みがき指導の様子の写真" style="background:linear-gradient(135deg,#d8cbb8,#a8b6c0)"></div><div class="body"><time>2020.03.10</time><h3>ブログの記事タイトルが入ります。ブログの記事タイトル</h3><p class="read">READ MORE</p></div></article>
    <article class="card"><div class="thumb" role="img" aria-label="歯ブラシの写真" style="background:linear-gradient(135deg,#f1e6ea,#d9a6b8)"></div><div class="body"><time>2020.03.02</time><h3>ブログの記事タイトルが入ります。ブログの記事タイトル</h3><p class="read">READ MORE</p></div></article>
    <article class="card"><div class="thumb" role="img" aria-label="街並みの風景写真" style="background:linear-gradient(180deg,#b9cbe0,#8e9a8a)"></div><div class="body"><time>2020.02.24</time><h3>ブログの記事タイトルが入ります。ブログの記事タイトル</h3><p class="read">READ MORE</p></div></article>
    <article class="card"><div class="thumb" role="img" aria-label="スタッフの写真" style="background:linear-gradient(135deg,#eef1f3,#d9c4b0)"></div><div class="body"><time>2020.02.15</time><h3>ブログの記事タイトルが入ります。ブログの記事タイトル</h3><p class="read">READ MORE</p></div></article>
  </div>
  <div class="card abs" style="left:1104px;top:120px;width:96px"><div class="thumb" role="img" aria-label="歯の模型の写真" style="background:linear-gradient(135deg,#cfe0ec,#f4f6f8)"></div></div>
  <a class="more-btn" style="color:var(--ink);text-decoration:none">MORE ›</a>
</section>

<nav class="banners">
  <a href="#"><svg width="22" height="22" viewBox="0 0 24 24" fill="none" stroke="#fff" stroke-width="1.5"><circle cx="12" cy="8" r="4"/><path d="M4 21c1-4.5 4-6.5 8-6.5s7 2 8 6.5"/></svg>求人情報</a>
  <a href="#"><svg width="24" height="22" viewBox="0 0 24 22" fill="none" stroke="#fff" stroke-width="1.5"><path d="M3 3h18v12H9l-5 4v-4H3z"/></svg>よくあるご質問</a>
  <a href="#"><svg width="24" height="18" viewBox="0 0 24 18" fill="none" stroke="#fff" stroke-width="1.5"><rect x="2" y="2" width="20" height="14"/><path d="M2 2l10 8 10-8"/></svg>お問い合わせ</a>
</nav>

<section class="access-sec">
  <div class="map" role="img" aria-label="医院周辺の地図"></div>
  <div class="clinic">
    <p class="name"><i></i>KOYOMIDAI DENTAL</p>
    <p class="addr">〒000-0000　東都府さくら市みどり町2-14-8</p>
    <p class="tel"><svg width="16" height="16" viewBox="0 0 24 24"><path d="M6.6 10.8a15 15 0 0 0 6.6 6.6l2.2-2.2a1 1 0 0 1 1-.25 11.4 11.4 0 0 0 3.6.57 1 1 0 0 1 1 1V20a1 1 0 0 1-1 1A17 17 0 0 1 3 4a1 1 0 0 1 1-1h3.5a1 1 0 0 1 1 1c0 1.25.2 2.45.57 3.6a1 1 0 0 1-.25 1z" fill="#7d6749"/></svg>03-5550-2184</p>
    <p class="hours">お問い合わせ・ご予約</p>
    <table>
      <tr><th></th><th>月</th><th>火</th><th>水</th><th>木</th><th>金</th><th>土</th><th>日</th></tr>
      <tr><td>09:30-13:00</td><td>○</td><td>○</td><td>○</td><td>－</td><td>○</td><td>○</td><td>－</td></tr>
      <tr><td>14:30-19:00</td><td>○</td><td>○</td><td>○</td><td>－</td><td>○</td><td>△</td><td>－</td></tr>
    </table>
  </div>
</section>

<footer class="site-footer">
  <div class="foot-nav">
    <ul><li>ホーム</li><li>当院について</li><li>医院紹介</li><li>スタッフ紹介</li><li>初めての方へ</li></ul>
    <ul><li>銀歯から自然な白い歯へ</li><li>歯医者にいけなくなった方へ</li><li>歯の色を全体的に白くしたい方へ</li><li>口臭が気になる方へ</li></ul>
    <ul><li>歯並びを整えたい方へ</li><li>歯が失ってしまった方へ</li><li>虫歯になってしまった方へ</li><li>お子様の歯を守りたい方へ</li></ul>
    <ul><li>お知らせ</li><li>ブログ</li></ul>
    <ul><li>求人情報</li><li>よくあるご質問</li><li>お問い合わせ</li><li>アクセス</li></ul>
  </div>
  <p class="copy">© KOYOMIDAI DENTAL ALL RIGHTS RESERVED.</p>
</footer>

</body>
</html>
```